Design NEW business card

We would like a business card using the colour deep red wine or dark navy blue textured background (patterned or not, open to suggestions) with a high gloss debossed rose gold/copper TM Thomas Marlow Jewellery business name (Provided). I have included images for your review we would like to keep our currently logo and business name on the front but you can change the layout and positioning. For the back of the card we are open to all suggestions/variations.
Use our current TM Thomas Marlow Jewellery logo (Provided image)

```html
<!DOCTYPE html>
<html lang="en">
<head>
<meta charset="utf-8">
<title>Thomas Marlow Jewellery – Business Card</title>
<link href="https://fonts.googleapis.com/css2?family=Montserrat:wght@300;400&family=Open+Sans:wght@400&display=swap" rel="stylesheet">
<style>
  :root {
    --backdrop: #cbae95;
    --wine: #541b23;
    --rose-gold: #b08660;
    --rose-gold-soft: #a57b58;
  }
  * { margin: 0; padding: 0; box-sizing: border-box; }
  html, body { width: 1200px; height: 1200px; overflow: hidden; }
  body { background: var(--backdrop); position: relative; font-family: "Open Sans", sans-serif; }

  .card {
    position: absolute;
    background: var(--wine);
    box-shadow: 0 14px 22px -12px rgba(60, 35, 20, 0.45);
  }
  .card--front { left: 281px; top: 182px; width: 634px; height: 361px; }
  .card--back  { left: 277px; top: 630px; width: 642px; height: 366px; }

  .brand {
    position: absolute;
    left: 0; right: 0;
    display: flex;
    align-items: center;
    justify-content: center;
    gap: 14px;
  }
  .card--front .brand { top: 168px; }
  .card--back .brand  { top: 150px; }

  .brand__dot {
    width: 12px; height: 12px;
    border-radius: 50%;
    background: var(--rose-gold);
  }
  .brand__name {
    font-family: "Montserrat", sans-serif;
    font-weight: 300;
    font-size: 19px;
    letter-spacing: 0.28em;
    color: var(--rose-gold);
    white-space: nowrap;
  }

  .holder {
    position: absolute;
    left: 41px; top: 280px;
    color: var(--rose-gold-soft);
  }
  .holder__name { font-size: 16px; line-height: 20px; }
  .holder__role { font-size: 12.5px; line-height: 18px; }

  .contact {
    position: absolute;
    right: 49px; top: 274px;
    text-align: right;
    list-style: none;
    color: var(--rose-gold-soft);
    font-size: 12px;
    line-height: 22px;
  }
</style>
</head>
<body>
  <section class="card card--front" aria-label="Card front">
    <div class="brand">
      <span class="brand__dot"></span>
      <span class="brand__name">THOMAS MARLOW JEWELLERY</span>
    </div>
  </section>

  <section class="card card--back" aria-label="Card back">
    <div class="brand">
      <span class="brand__dot"></span>
      <span class="brand__name">THOMAS MARLOW JEWELLERY</span>
    </div>
    <div class="holder">
      <p class="holder__name">Your Full Name</p>
      <p class="holder__role">Designation</p>
    </div>
    <ul class="contact">
      <li>(02)+ 98-765-432</li>
      <li>info@tmjewellery.com</li>
      <li>www.tmjewellery.com</li>
    </ul>
  </section>
</body>
</html>
```